Urkundendesign für Jahrgangsbeste einer Realschule gesucht
Der Elternbeirat der Realschule Lindwerth benötigt für die Jahrgangsbesten des Abschlussjahrgangs eine Urkunde. Gerne mit Prägung (was kostet sowas bei Druck?!?). Das von-Halmberg-Logo darf benutzt werden (siehe Homepage).
es soll eine Urkunde für den/die 'Jahrgangsbeste 2026' geben. das Datum, sowie SchülerInnen-Name würden wir jeweils handschriftlich anbringen.
die Urkunde in A4 gestalten.
wir benötigen die üblichen druckbaren Dateien, sodass eine Druckerei dann auch selbst Jahr für Jahr das Jahr abändern kann.
bitte um Vorschläge, wir arbeiten uns nach und nach da durch.
nicht zu viel Schnörkelei.

```html
<!DOCTYPE html>
<html lang="de">
<head>
<meta charset="utf-8">
<title>Urkunde Jahrgangsbester – Realschule Lindwerth</title>
<link rel="stylesheet" href="https://fonts.googleapis.com/css2?family=Cinzel:wght@400&family=Fira+Sans+Condensed:wght@300;400;700&family=Outfit:wght@300&display=swap">
<style>
  :root {
    --page-bg: #ffffff;
    --panel-bg: #f7f7f7;
    --sheet-bg: #ffffff;
    --band-yellow: #fbc50a;
    --brand-green: #55ac33;
    --brand-red: #d70f1e;
    --ink: #1a1a1a;
    --rule: #9a9a9a;
    --caption: #9a9a9a;
  }
  * { margin: 0; padding: 0; box-sizing: border-box; }
  html, body { width: 1200px; height: 1200px; overflow: hidden; background: var(--page-bg); }
  .canvas { position: relative; width: 1200px; height: 1200px; }
  .panel { position: absolute; left: 82px; top: 82px; width: 1043px; height: 1043px; background: var(--panel-bg); }

  .certificate { position: absolute; left: 316px; top: 131px; width: 575px; height: 812px; background: var(--sheet-bg); overflow: hidden; }

  .side-band { position: absolute; left: 0; top: 0; width: 157px; height: 812px; background: var(--band-yellow); }
  .side-band__head { position: absolute; left: 0; top: 0; width: 143px; height: 89px; background: var(--brand-green);
    display: flex; align-items: center; justify-content: center; }
  .side-band__accent { position: absolute; left: 143px; top: 0; width: 14px; height: 89px; background: var(--brand-red); }
  .school-mark--inverse { font-family: "Fira Sans Condensed", sans-serif; font-weight: 700; font-size: 15px; color: #fff; letter-spacing: 0.5px; }

  .side-band__title { position: absolute; left: 45px; top: 138px; width: 70px; height: 619px;
    display: flex; flex-direction: column-reverse; justify-content: space-between; align-items: center; }
  .side-band__letter { display: block; width: 70px; height: 70px; line-height: 70px; text-align: center;
    font-family: "Cinzel", serif; font-size: 72px; color: #fff; transform: rotate(-90deg); }

  .school-mark { position: absolute; right: 22px; top: 32px; text-align: right;
    font-family: "Fira Sans Condensed", sans-serif; font-weight: 700; font-size: 15px; line-height: 1.2; color: var(--brand-green); }

  .content { position: absolute; left: 196px; top: 0; width: 340px; font-family: "Fira Sans Condensed", sans-serif; font-weight: 300; color: var(--ink); }
  .eyebrow { position: absolute; top: 202px; font-size: 8.5px; white-space: nowrap; letter-spacing: 0.3px; }
  .award-title { position: absolute; top: 213px; font-family: "Cinzel", serif; font-weight: 400; font-size: 32px; letter-spacing: 2.6px; white-space: nowrap; }
  .field { position: absolute; width: 334px; }
  .field__line { height: 0; border-top: 1px dotted var(--rule); }
  .field__line--solid { border-top: 1px solid var(--rule); }
  .field__label { font-size: 8.5px; margin-top: 6px; letter-spacing: 0.3px; }
  .field--name { top: 360px; }
  .field--date { top: 642px; }
  .citation { position: absolute; top: 427px; width: 318px; font-size: 8.5px; line-height: 12.8px; letter-spacing: 0.3px; }

  .signature { position: absolute; left: -8px; top: 689px; width: 76px; height: 46px; background: linear-gradient(90deg, #e4e4e4, #f2f2f2); }
  .signatory { position: absolute; top: 743px; font-size: 8.5px; line-height: 10.5px; letter-spacing: 0.3px; }
  .signatory__name { font-weight: 700; }

  .caption { position: absolute; left: 82px; top: 985px; width: 1043px; text-align: center;
    font-family: "Outfit", sans-serif; font-weight: 300; font-size: 14.5px; line-height: 21px; color: var(--caption); }
</style>
</head>
<body>
<div class="canvas">
  <div class="panel"></div>

  <article class="certificate">
    <aside class="side-band">
      <div class="side-band__head"><span class="school-mark--inverse">Lindwerth</span></div>
      <div class="side-band__accent"></div>
      <div class="side-band__title" aria-label="URKUNDE">
        <span class="side-band__letter">U</span>
        <span class="side-band__letter">R</span>
        <span class="side-band__letter">K</span>
        <span class="side-band__letter">U</span>
        <span class="side-band__letter">N</span>
        <span class="side-band__letter">D</span>
        <span class="side-band__letter">E</span>
      </div>
    </aside>

    <div class="school-mark">Realschule<br>Lindwerth</div>

    <section class="content">
      <p class="eyebrow">Lorem ipsum dolor sit amet</p>
      <h1 class="award-title">JAHRGANGSBESTER</h1>

      <div class="field field--name">
        <div class="field__line"></div>
        <p class="field__label">Schülername</p>
      </div>

      <p class="citation">Lorem ipsum dolor sit amet, consectetuer adipiscing elit, sed diam nonummy nibh euismod tincidunt ut laoreet dolore magna aliquam erat volutpat. Ut wisi enim ad minim veniam, quis nostrud.</p>

      <div class="field field--date">
        <div class="field__line field__line--solid"></div>
        <p class="field__label">Datum</p>
      </div>

      <div class="signature" role="img" aria-label="Handschriftliche Unterschrift des Schulleiters"></div>
      <p class="signatory"><span class="signatory__name">Max Mustermann</span><br>Schulleiter</p>
    </section>
  </article>

  <p class="caption">Lorem ipsum dolor sit amet, consetetur sadipscing elitr, sed diam nonumy eirmod tempor invidunt<br>ut labore et dolore magna aliquyam erat, sed diam voluptua. At vero eos et accusam et justo duo<br>dolores et ea rebum. Stet clita kasd gubergren, no sea takimata sanctus est.</p>
</div>
</body>
</html>
```